Business Card Design for Occupational Medicine Start Up Company

We need to design a professional business card. We are a healthcare company providing occupational medicine services to blue collar industries. We are professional, efficient and high quality service providers.

Target Market(s)

Blue Collar Industry: Shipbuilding, Ports, Trucking Companies; The Executives and Safety Officers for these companies

Industry/Entity Type

Healthcare

Contact Information for Business Card

Logo, Name, Title, Email, Phone

Other font styles liked:
• Please match our Brand Guide

Requirements
Must have
• Our Company Colors and Logo

```html
<!DOCTYPE html>
<html lang="en">
<head>
<meta charset="utf-8">
<title>CrewWell Business Card</title>
<link href="https://fonts.googleapis.com/css2?family=Barlow:wght@400;500;700&display=swap" rel="stylesheet">
<style>
  :root {
    --navy: #2b347c;
    --orange: #f2af4e;
    --paper: #fbfbfb;
    --gap: #ffffff;
    --ink-grey: #6d6e71;
    --white: #ffffff;
  }
  * { margin: 0; padding: 0; box-sizing: border-box; }
  html, body {
    width: 1200px; height: 355px; overflow: hidden;
    background: var(--gap);
    font-family: "Barlow", Arial, sans-serif;
  }
  .canvas { position: relative; width: 1200px; height: 355px; }

  .card { position: absolute; top: 0; height: 355px; background: var(--paper); }
  .card--front { left: 0; width: 585px; }
  .card--back { left: 615px; width: 585px; }

  .accent-bar { position: absolute; width: 10px; height: 60px; background: var(--orange); }
  .accent-bar--tl1 { left: 59px; top: 0; }
  .accent-bar--tl2 { left: 76px; top: 0; }
  .accent-bar--br1 { left: 498px; top: 292px; }
  .accent-bar--br2 { left: 516px; top: 292px; }

  .brand {
    position: absolute; left: 0; right: 0; top: 148px;
    display: flex; align-items: center; justify-content: center; gap: 14px;
  }
  .brand__dot { width: 26px; height: 26px; border-radius: 50%; background: var(--orange); }
  .brand__name {
    font-weight: 700; font-size: 42px; letter-spacing: 1px; color: var(--navy);
  }

  .side-panel {
    position: absolute; left: 0; top: 0; width: 254px; height: 355px;
    background: var(--navy);
    display: flex; align-items: center; justify-content: center;
  }
  .side-panel__name {
    font-weight: 700; font-size: 32px; letter-spacing: 1px; color: var(--white);
    margin-top: -40px;
  }
  .side-stripe {
    position: absolute; left: 254px; top: 0; width: 24px; height: 355px;
    background: var(--orange);
  }

  .holder-name {
    position: absolute; left: 309px; top: 82px;
    font-weight: 700; font-size: 24px; letter-spacing: 2px; color: var(--navy);
  }
  .contact-list { position: absolute; left: 300px; top: 160px; list-style: none; }
  .contact-list li {
    display: flex; align-items: flex-start; gap: 12px;
    font-size: 14.5px; font-weight: 500; letter-spacing: 1.3px;
    color: var(--ink-grey); line-height: 17px; margin-bottom: 7px;
  }
  .contact-list svg { width: 12px; height: 12px; flex: none; margin-top: 3px; fill: var(--orange); }
</style>
</head>
<body>
<div class="canvas">
  <section class="card card--front">
    <span class="accent-bar accent-bar--tl1"></span>
    <span class="accent-bar accent-bar--tl2"></span>
    <div class="brand">
      <span class="brand__dot"></span>
      <span class="brand__name">CREWWELL</span>
    </div>
    <span class="accent-bar accent-bar--br1"></span>
    <span class="accent-bar accent-bar--br2"></span>
  </section>

  <section class="card card--back">
    <div class="side-panel"><span class="side-panel__name">CREWWELL</span></div>
    <div class="side-stripe"></div>
    <h1 class="holder-name">DANA WHITFIELD</h1>
    <ul class="contact-list">
      <li>
        <svg viewBox="0 0 24 24" aria-hidden="true"><path d="M6.6 10.8c1.4 2.8 3.8 5.1 6.6 6.6l2.2-2.2c.3-.3.7-.4 1-.2 1.1.4 2.3.6 3.6.6.6 0 1 .4 1 1V20c0 .6-.4 1-1 1C10.6 21 3 13.4 3 4c0-.6.4-1 1-1h3.5c.6 0 1 .4 1 1 0 1.3.2 2.5.6 3.6.1.3 0 .7-.2 1z"/></svg>
        <span>555 014 2290</span>
      </li>
      <li>
        <svg viewBox="0 0 24 24" aria-hidden="true"><path d="M2 5h20v14H2z M3.5 6.5 12 13l8.5-6.5" fill="var(--orange)"/><path d="M3.5 6.5 12 13l8.5-6.5" fill="none" stroke="#fff" stroke-width="1.5"/></svg>
        <span>hello@crewwellmail.com</span>
      </li>
      <li>
        <svg viewBox="0 0 24 24" aria-hidden="true"><g fill="none" stroke="var(--orange)" stroke-width="1.8"><circle cx="12" cy="12" r="10"/><ellipse cx="12" cy="12" rx="4.5" ry="10"/><path d="M2 12h20M4 7h16M4 17h16"/></g></svg>
        <span>www.crewwellhealth.com</span>
      </li>
      <li>
        <svg viewBox="0 0 24 24" aria-hidden="true"><path d="M12 2a7 7 0 0 0-7 7c0 5.2 7 13 7 13s7-7.8 7-13a7 7 0 0 0-7-7zm0 9.5A2.5 2.5 0 1 1 12 6.5a2.5 2.5 0 0 1 0 5z"/></svg>
        <span>210 Harbor Street,<br>Newport, NC</span>
      </li>
    </ul>
  </section>
</div>
</body>
</html>
```